Flyer for an IT consultancy firm

We are an IT consultancy firm based in Iceland. We have a website at: www.brimvolt.com where you can get acquainted with our activities.
We require a double-sided flyer in A4 format to be handed out in conferences, trade shows etc. The flyer is basically a summarized overview of our range of services.

The deliverable should incorporate some visual elements that are relevant to our line of business such as:
• computers
• cybersecurity
• networks
Also, it would be nice to have visuals relating to Icelandic geography, to further emphasize our local roots. Some suggested keywords:
• volcano
• aurora borealis
• waterfall
• glacier

NB: the flyer will be printed out, therefore image resolution needs to be high enough to render nicely on paper.
The primary colors would be red, black and white – in line with our logo. But there is freedom to diverge and go for a different color scheme.

The logo should be present on the top front of the flyer. The URL www.brimvolt.com needs to be mentioned prominently, for example at the bottom of the page.

Examples of design we like:
• https://www.pixelbazaar.net/design/24252027
• https://www.pixelbazaar.net/design/24291120

Attached:
• the text for the brochure in PDF format
• our logo in vector format

IT, software, cybersecurity

EB3D1F
EC4F4E
F09395
F8D3D4
FCEDEE

• existing logo, and visuals related to computer, networks etc
• Icelandic geography/landscapes

```html
<!DOCTYPE html>
<html lang="en">
<head>
<meta charset="utf-8">
<title>Brimvolt – IT Consultancy Flyer</title>
<link rel="stylesheet" href="https://fonts.googleapis.com/css2?family=Montserrat:wght@400;500;600;700;800&display=swap">
<style>
  :root {
    --stage: #e6e6e8;
    --paper: #ffffff;
    --brand-red: #9e1b21;
    --brand-black: #0e0e0f;
    --ink: #222225;
    --white: #ffffff;
    --ring: #d9d9db;
    --photo-blue: #0d3f73;
    --photo-dark: #120a10;
    --photo-red: #6a1016;
  }
  * { margin: 0; padding: 0; box-sizing: border-box; }
  html, body { width: 1200px; height: 1200px; overflow: hidden; }
  body {
    background: var(--stage);
    font-family: "Montserrat", sans-serif;
    position: relative;
  }
  .flyer {
    position: absolute;
    left: 217px; top: 59px;
    width: 765px; height: 1082px;
    background: linear-gradient(180deg, var(--paper) 0%, #f6f6f7 55%, #f1f1f2 100%);
    overflow: hidden;
  }
  .flyer-shapes { position: absolute; left: 0; top: 0; }
  .brand {
    position: absolute;
    left: 45px; top: 41px;
    width: 216px;
    display: flex; flex-direction: column; align-items: center; gap: 16px;
  }
  .brand-dot {
    width: 71px; height: 71px;
    border: 3px solid var(--brand-red);
    border-radius: 50%;
  }
  .brand-name {
    font-weight: 800;
    font-size: 35px;
    letter-spacing: 1px;
    color: var(--brand-black);
    line-height: 1;
  }
  .headline {
    position: absolute;
    left: 44px; top: 351px;
    color: var(--white);
    font-weight: 700;
    font-size: 27px;
    line-height: 34px;
    letter-spacing: 0.5px;
    text-transform: uppercase;
  }
  .service {
    position: absolute;
    text-align: center;
  }
  .service-title {
    color: var(--brand-red);
    font-weight: 700;
    font-size: 25px;
    line-height: 1;
    text-transform: uppercase;
  }
  .service-text {
    margin-top: 14px;
    color: var(--ink);
    font-size: 11px;
    line-height: 13.5px;
  }
  .service--computers { left: 43px; top: 670px; width: 300px; }
  .service--security { left: 434px; top: 670px; width: 300px; }
  .service--networks { left: 100px; top: 882px; width: 566px; }
  .contact {
    position: absolute;
    color: var(--white);
  }
  .contact--phone {
    left: 99px; top: 1029px;
    font-weight: 600;
    font-size: 21px;
  }
  .contact--address {
    left: 546px; top: 1024px;
    font-size: 15px;
    line-height: 19px;
  }
</style>
</head>
<body>
  <main class="flyer">
    <svg class="flyer-shapes" width="765" height="1082" viewBox="0 0 765 1082" xmlns="http://www.w3.org/2000/svg">
      <defs>
        <linearGradient id="photoTone" x1="0" y1="0" x2="1" y2="0.3">
          <stop offset="0" stop-color="var(--photo-blue)"/>
          <stop offset="0.4" stop-color="var(--photo-dark)"/>
          <stop offset="1" stop-color="var(--photo-red)"/>
        </linearGradient>
        <radialGradient id="badgeRing" cx="0.5" cy="0.45" r="0.55">
          <stop offset="0.8" stop-color="#ffffff"/>
          <stop offset="1" stop-color="var(--ring)"/>
        </radialGradient>
      </defs>

      <g role="img" aria-label="Circuit board with glowing red and blue server icons">
        <polygon points="408,0 765,0 765,519 439,519 280,233" fill="url(#photoTone)"/>
      </g>
      <polygon class="accent-strip" points="520,519 765,519 765,566 548,566" fill="var(--brand-red)"/>
      <polygon class="headline-band" points="0,333 412,333 440,501 0,501" fill="var(--brand-red)"/>

      <g class="badge badge--computers" transform="translate(193 626)">
        <circle r="37" fill="url(#badgeRing)"/>
        <circle r="29" fill="var(--brand-red)"/>
        <rect x="-12" y="-10" width="24" height="16" rx="1.5" fill="none" stroke="#fff" stroke-width="2"/>
        <path d="M-4 10 h8 M0 6 v4" stroke="#fff" stroke-width="2" fill="none"/>
      </g>
      <g class="badge badge--security" transform="translate(584 626)">
        <circle r="37" fill="url(#badgeRing)"/>
        <circle r="29" fill="var(--brand-red)"/>
        <rect x="-11" y="-3" width="16" height="13" rx="1.5" fill="none" stroke="#fff" stroke-width="2"/>
        <path d="M-7 -3 v-4 a4 4 0 0 1 8 0 v4" fill="none" stroke="#fff" stroke-width="2"/>
        <path d="M8 -4 h6 M8 2 h7 M8 8 h5" stroke="#fff" stroke-width="1.6"/>
      </g>
      <g class="badge badge--networks" transform="translate(383 838)">
        <circle r="37" fill="url(#badgeRing)"/>
        <circle r="29" fill="var(--brand-red)"/>
        <g stroke="#fff" stroke-width="1.8" fill="none">
          <path d="M0 0 L-10 -10 M0 0 L10 -9 M0 0 L-9 10 M0 0 L11 8"/>
          <circle r="3.5"/>
          <circle cx="-11" cy="-11" r="2.8"/>
          <circle cx="11" cy="-10" r="2.8"/>
          <circle cx="-10" cy="11" r="2.8"/>
          <circle cx="12" cy="9" r="2.8"/>
        </g>
      </g>

      <polygon class="footer-phone" points="0,995 362,995 410,1082 0,1082" fill="var(--brand-black)"/>
      <polygon class="footer-address" points="432,995 765,995 765,1082 410,1082" fill="var(--brand-red)"/>

      <g class="icon-phone" transform="translate(60 1041)" fill="none" stroke="#fff" stroke-width="2.4" stroke-linecap="round">
        <path d="M-9 -10 l5 -2 l4 7 l-3 3 a14 14 0 0 0 6 6 l3 -3 l7 4 l-2 5 c-12 2 -24 -10 -20 -20 z" fill="#fff" stroke="none"/>
        <path d="M4 -9 a8 8 0 0 1 6 6 M5 -14 a13 13 0 0 1 10 10"/>
      </g>
      <g class="icon-pin" transform="translate(498 1041)" fill="none" stroke="#fff" stroke-width="2.2">
        <path d="M0 8 c-6 -7 -9 -11 -9 -15 a9 9 0 0 1 18 0 c0 4 -3 8 -9 15 z"/>
        <circle cx="0" cy="-7" r="3"/>
        <path d="M-7 6 l-6 7 h26 l-6 -7"/>
      </g>
    </svg>

    <div class="brand">
      <span class="brand-dot"></span>
      <span class="brand-name">BRIMVOLT</span>
    </div>

    <h1 class="headline">Your Icelandic<br>partner in<br>cybersecurity<br>and IT consultancy</h1>

    <section class="service service--computers">
      <h2 class="service-title">Computers</h2>
      <p class="service-text">Lorem ipsum dolor sit amet, consectetuer adipiscing elit, sed diam nonummy nibh euismod tincidunt ut laoreet dolore magna aliquam erat volutpat. Ut wisi enim ad minim veniam, quis nostrud exerci tation ullamcorper suscipit lobortis nisl ut aliquip ex ea</p>
    </section>
    <section class="service service--security">
      <h2 class="service-title">Cybersecurity</h2>
      <p class="service-text">Lorem ipsum dolor sit amet, consectetuer adipiscing elit, sed diam nonummy nibh euismod tincidunt ut laoreet dolore magna aliquam erat volutpat. Ut wisi enim ad minim veniam, quis nostrud exerci tation ullamcorper suscipit lobortis nisl ut aliquip ex ea</p>
    </section>
    <section class="service service--networks">
      <h2 class="service-title">Networks</h2>
      <p class="service-text">Lorem ipsum dolor sit amet, consectetuer adipiscing elit, sed diam nonummy nibh euismod tincidunt<br>ut laoreet dolore magna aliquam erat volutpat. Ut wisi enim ad minim veniam, quis nostrud exerci<br>tation ullamcorper suscipit lobortis nisl ut aliquip ex ea</p>
    </section>

    <p class="contact contact--phone">+354 5550142</p>
    <p class="contact contact--address">Brimvolt ehf, Hraunholt 14<br>310 Borgarvík, Iceland</p>
  </main>
</body>
</html>
```